Fabric Store Business card

Need a business card portraying store logo and up and coming business of quilt fabrics, apparel fabrics, notions and buttons. Our business name is Gilded Thimble and Such. Am attaching logo. The design should communicate a growing business and warm atmosphere. Would like address and store hours and contact info displayed on card. Mon - Fri 9:30 to 5:00, Saturday 9:30 to 1:00. Address 287 W Alder Ave, Newton, KS 67392 email: gildedthimbleandsuch@mailbrook.net. Phone and fax 316-555-2846. After hours contact # 620-555-3914 Also like vintage sewing machines and dress forms if it works to incorporate fine, if not thats ok too.

```html
<!DOCTYPE html>
<html lang="en">
<head>
<meta charset="utf-8">
<title>Gilded Thimble and Such — Business Card</title>
<link rel="stylesheet" href="https://fonts.googleapis.com/css2?family=Dancing+Script:wght@400;500&display=swap">
<style>
  :root {
    --card-tan: #9c6e42;
    --card-shadow-tone: #8d5f37;
    --brand-red: #6e0508;
    --ink: #0d0906;
  }
  html, body {
    margin: 0;
    padding: 0;
    width: 1200px;
    height: 737px;
    overflow: hidden;
    background: var(--card-tan);
  }
  .card {
    position: relative;
    width: 1200px;
    height: 737px;
    background: var(--card-tan);
    overflow: hidden;
    font-family: "Dancing Script", cursive;
  }
  .card__backdrop {
    position: absolute;
    left: 0;
    top: 0;
    width: 1200px;
    height: 737px;
  }
  .brand {
    position: absolute;
    left: 0;
    top: 0;
    width: 1200px;
    height: 737px;
    margin: 0;
  }
  .brand__dot {
    position: absolute;
    left: 290px;
    top: 277px;
    width: 114px;
    height: 114px;
    border-radius: 50%;
    background: var(--brand-red);
  }
  .brand__name {
    margin: 0;
    font-weight: 400;
    color: var(--brand-red);
    font-size: 76px;
    line-height: 76px;
    white-space: nowrap;
  }
  .brand__name-line {
    position: absolute;
    display: block;
  }
  .brand__name-line--first {
    left: 412px;
    top: 288px;
  }
  .brand__name-line--second {
    left: 632px;
    top: 346px;
  }
  .offerings {
    position: absolute;
    left: 0;
    top: 561px;
    width: 1200px;
    height: 80px;
    display: flex;
    justify-content: center;
    align-items: center;
    margin: 0;
    padding: 0;
    list-style: none;
  }
  .offerings__item {
    font-size: 46px;
    color: var(--ink);
    padding: 0 20px;
    line-height: 80px;
  }
  .offerings__item + .offerings__item {
    border-left: 3px solid var(--ink);
  }
</style>
</head>
<body>
  <main class="card">
    <svg class="card__backdrop" viewBox="0 0 1200 737" role="img" aria-label="Faint tone-on-tone scissors illustration across the lower right of the card">
      <defs>
        <radialGradient id="backdrop-glow" cx="0.78" cy="0.75" r="0.6">
          <stop offset="0" stop-color="#8d5f37" stop-opacity="0.85"/>
          <stop offset="1" stop-color="#9c6e42" stop-opacity="0"/>
        </radialGradient>
      </defs>
      <rect x="0" y="0" width="1200" height="737" fill="url(#backdrop-glow)"/>
    </svg>

    <header class="brand">
      <span class="brand__dot" aria-hidden="true"></span>
      <h1 class="brand__name">
        <span class="brand__name-line brand__name-line--first">Gilded Thimble</span>
        <span class="brand__name-line brand__name-line--second">and Such</span>
      </h1>
    </header>

    <ul class="offerings">
      <li class="offerings__item">quilt fabrics</li>
      <li class="offerings__item">apparel fabrics</li>
      <li class="offerings__item">notions and buttons</li>
    </ul>
  </main>
</body>
</html>
```